Commercial Construction Company

We need a business card design based on our current logo. We are a commercial general contractor based in Southern California that specializes in bank remodels. We would like to see designs that incorporate dark blue. The final design should portray an image of professionalism and quality.

If possible, I would like to add metallic foil to the design. Thank you

```html
<!DOCTYPE html>
<html lang="en">
<head>
<meta charset="utf-8">
<title>Business Card – Front and Back</title>
<link href="https://fonts.googleapis.com/css2?family=Arimo:wght@400;700&display=swap" rel="stylesheet">
<style>
  :root {
    --page-bg: #e9eaec;
    --card-white: #ffffff;
    --navy: #053b78;
    --blue-mid: #1c5691;
    --blue-light: #3a6fa5;
    --text-blue: #0d4a8a;
    --shadow: rgba(20, 30, 50, 0.18);
  }
  * { box-sizing: border-box; margin: 0; padding: 0; }
  html, body {
    width: 1200px;
    height: 873px;
    overflow: hidden;
    background: var(--page-bg);
  }
  .sheet {
    width: 1200px;
    height: 873px;
    display: flex;
    align-items: center;
    justify-content: center;
    gap: 50px;
  }
  .card {
    position: relative;
    width: 540px;
    height: 315px;
    background: var(--card-white);
    box-shadow: 0 6px 22px var(--shadow);
    overflow: hidden;
  }
  .card-art {
    position: absolute;
    inset: 0;
    width: 100%;
    height: 100%;
  }
  .front-decor {
    position: absolute;
    left: 220px;
    top: 160px;
    width: 380px;
    height: 380px;
    border-radius: 50%;
    background: radial-gradient(circle at 50% 50%, var(--blue-light) 0%, var(--blue-mid) 55%, var(--navy) 100%);
  }
  .front-copy {
    position: absolute;
    left: 34px;
    top: 34px;
    width: 330px;
    font-family: "Arimo", Arial, sans-serif;
    font-size: 19px;
    line-height: 1.3;
    color: var(--text-blue);
    text-align: justify;
  }
  .brand-lockup {
    position: absolute;
    left: 50%;
    top: 50%;
    transform: translate(-50%, -50%);
    display: flex;
    align-items: center;
    gap: 12px;
    white-space: nowrap;
  }
  .brand-dot {
    flex: 0 0 22px;
    width: 22px;
    height: 22px;
    border-radius: 50%;
    background: var(--navy);
  }
  .brand-name {
    font-family: "Arimo", Arial, sans-serif;
    font-weight: 700;
    font-size: 28px;
    letter-spacing: 1px;
    color: var(--navy);
  }
</style>
</head>
<body>
  <main class="sheet">
    <section class="card card-front" aria-label="Card front">
      <div class="front-decor" role="img" aria-label="Decorative blue circular graphic"></div>
      <p class="front-copy">Lorem Ipsum is simply dummy text of the printing and typesetting industry. Lorem Ipsum has been the industry's standard dummy text ever since the 1500s, when an unknown</p>
    </section>

    <section class="card card-back" aria-label="Card back">
      <svg class="card-art" viewBox="0 0 540 315" aria-hidden="true">
        <circle cx="70" cy="0" r="52" fill="var(--navy)"/>
        <circle cx="470" cy="315" r="52" fill="var(--navy)"/>
      </svg>
      <div class="brand-lockup">
        <span class="brand-dot"></span>
        <span class="brand-name">Marlow Build Group</span>
      </div>
    </section>
  </main>
</body>
</html>
```